Dental Practice Billboard Design

We are a newer dental practice in need of a simple but appealing billboard for our growing dental practice to attract new patients. The practice is owned by husband and wife dentists and is family friendly in a small town in Kentucky. We try to be very friendly and caring to our patients. Would prefer a blue background for the billboard and our tooth logo to be prominent. We are partial to the Patua One font used in the image below but please feel free to tweak it as you deem necessary. The shape of the uppercase D and lowercase g are why we like that font, so fonts with a similarly shaped “D” and “g” would work as well. Please include our phone number (606) 847-3962. Please see our website Harlowfamilydentistry.com for more info on the practice if needed. Thank you! Looking forward to seeing your creation.
Updates

The dimensions will be 12ft x 24ft (3.6576m x 7.3152m). Apologies for not including this in the original prompt. Thank you all for your submissions.

Industry/Entity Type

Dental

Font styles to use
Other font styles liked:
• Patua One

Colors
0054AA
0677BA
7BADD7
CADEEF
E8F1F8
0094D4
00A9DD
6FCCEA
C7EBF8
E9F6FB
00AB8E
00BBA5
67D7C9
C6EFE9
E9F9F6
59FF00
82FF00
B8FF75
E3FFCB
F4FFEA

Requirements
Must have
• Phone number, website, Logo, Practice name “Harlow Family Dentistry”
Should not have
• A tagline or slogan

```html
<!DOCTYPE html>
<html lang="en">
<head>
<meta charset="utf-8">
<title>Harlow Family Dentistry – Billboard</title>
<link rel="stylesheet" href="https://fonts.googleapis.com/css2?family=Fira+Sans:wght@600&family=Patua+One&display=swap">
<style>
  :root {
    --page: #ffffff;
    --brand-blue: #0a4ea8;
    --deep-blue: #073f8f;
    --bright-blue: #0a84e0;
    --sky-blue: #2ea2ee;
    --pale-blue: #7badd7;
    --leaf-green: #2f6e1c;
    --lime: #9bd43a;
    --green: #1aab22;
    --white: #ffffff;
  }
  html, body {
    margin: 0;
    width: 852px;
    height: 1200px;
    overflow: hidden;
    background: var(--page);
  }
  .billboard {
    position: absolute;
    left: 76px;
    top: 122px;
    width: 734px;
    height: 357px;
    box-shadow: 0 10px 30px rgba(0,0,0,0.12);
    outline: 1px solid #333;
  }
  .billboard svg { display: block; width: 100%; height: 100%; }
  .brand-name { font-family: "Patua One", serif; fill: var(--brand-blue); }
  .website { font-family: "Patua One", serif; fill: var(--leaf-green); }
  .phone-number { font-family: "Fira Sans", sans-serif; font-weight: 600; fill: var(--white); }
</style>
</head>
<body>
<div class="billboard">
  <svg viewBox="0 0 734 357" xmlns="http://www.w3.org/2000/svg">
    <defs>
      <linearGradient id="cornerGreen" x1="0" y1="0" x2="1" y2="1">
        <stop offset="0" stop-color="#a9d86a"/>
        <stop offset="1" stop-color="#ffffff" stop-opacity="0"/>
      </linearGradient>
      <linearGradient id="cornerBlue" x1="0" y1="1" x2="1" y2="0">
        <stop offset="0" stop-color="#4f93dc"/>
        <stop offset="1" stop-color="#e8f1f8"/>
      </linearGradient>
      <linearGradient id="bandBlue" x1="0" y1="0" x2="0" y2="1">
        <stop offset="0" stop-color="#063f8c"/>
        <stop offset="1" stop-color="#0a54b6"/>
      </linearGradient>
      <linearGradient id="swooshGreen" x1="0" y1="0" x2="0" y2="1">
        <stop offset="0" stop-color="#b8e35a"/>
        <stop offset="1" stop-color="#14ab1c"/>
      </linearGradient>
      <linearGradient id="swooshBlue" x1="0" y1="0" x2="0" y2="1">
        <stop offset="0" stop-color="#1597ea"/>
        <stop offset="1" stop-color="#0a4fb0"/>
      </linearGradient>
      <linearGradient id="photoTone" x1="0" y1="0" x2="1" y2="1">
        <stop offset="0" stop-color="#c9ced3"/>
        <stop offset="0.5" stop-color="#e2c8ba"/>
        <stop offset="1" stop-color="#d9b19c"/>
      </linearGradient>
    </defs>

    <rect class="background" width="734" height="357" fill="var(--white)"/>

    <!-- corner accents -->
    <path class="corner-green" d="M0 0 H95 C75 50 45 90 0 112 Z" fill="url(#cornerGreen)"/>
    <path class="corner-swoosh" d="M0 132 C45 112 82 70 100 0 H108 C92 80 60 150 0 246 Z" fill="url(#cornerBlue)"/>

    <!-- contact band -->
    <rect class="contact-band" x="0" y="249" width="430" height="108" fill="url(#bandBlue)"/>
    <rect class="contact-band-edge" x="0" y="248" width="430" height="3" fill="var(--bright-blue)"/>

    <!-- right swooshes -->
    <path class="swoosh-green" d="M483 0 C430 70 395 170 392 251 C391 300 393 330 398 357 H734 V0 Z" fill="url(#swooshGreen)"/>
    <path class="swoosh-blue" d="M505 0 C455 80 420 180 420 260 C420 300 428 330 450 357 H734 V0 Z" fill="url(#swooshBlue)"/>
    <path class="swoosh-light" d="M520 0 C480 80 460 190 475 270 C485 310 505 340 525 357 H734 V0 Z" fill="var(--sky-blue)" opacity="0.55"/>
    <path class="swoosh-inner" d="M512 0 C482 70 478 170 500 250 C520 310 560 340 600 357 H734 V0 Z" fill="#0d6fd4"/>

    <!-- photo area -->
    <path class="photo" role="img" aria-label="Photo: smiling patient having teeth checked with a dental mirror"
          d="M510 0 H734 V357 H677 C570 330 485 240 482 140 C481 80 492 35 510 0 Z" fill="url(#photoTone)"/>

    <!-- practice name -->
    <circle class="brand-dot" cx="116" cy="62" r="28" fill="var(--brand-blue)"/>
    <text class="brand-name" x="166" y="70" font-size="44">Harlow</text>
    <text class="brand-name" x="162" y="100" font-size="22">Family Dentistry</text>

    <!-- website -->
    <text class="website" x="226" y="196" font-size="28" text-anchor="middle">Harlowfamilydentistry.com</text>

    <!-- phone -->
    <g class="phone-icon" fill="none" stroke="var(--lime)" stroke-width="1.6">
      <circle cx="64" cy="302" r="17"/>
      <path d="M59 293 L63 292 L65 298 L62 300 C63 304 65 306 68 308 L70 305 L76 307 L75 311 C66 312 56 302 59 293 Z"/>
    </g>
    <text class="phone-number" x="101" y="316" font-size="33">(606) 847-3962.</text>
  </svg>
</div>
</body>
</html>
```